Bootstrap site for Cloud Services company

Hi,

First I'd like you to submit you design of the homepage. If you are the winner, I'll get you do design the rest and code it up in HTML, CSS etc using bootstrap.

Why bootstrap? This will probably mean
that you understand the fundamentals of CSS and know how to
make a good-looking website. Also should mean that you can throw
together this site relatively easily so you can focus on the design
work. I'll need some icons and banner style images done.

There's no server-side coding involved, and there's also no content to write, just put placemarker text wherever appropriate. You must be familiar with bootstrap.

Our business sells Varnel Suite for Business and IT support services.

The icon for our business is attached.

Basically I want you to go by the design of this site
http://lnk.example-short.test/kQ7r

However, don't just copy it. I want it to be of a similar layout and
style, but be creative.

I like the simplicity and how it's easy to follow visually.

Just submit the homepage, and if you're successful, I'll get you to
design the rest of the pages for me and code up the pages.

Thanks!

Target Market(s)

We are marketing towards businesses that need their IT managed for them.

Industry/Entity Type

Business

Requirements
Must have
• I like how clean and nice the roboto font is, but it's up to you.

You're welcome to take inspiration from the 'Varnel Pulse' layout and design. Nice use of white space and layout.

Menu headings at the top are as follows:
Support | Deployment | Training | Development | Contact Us |
About

Home page:

In a similar style of the referenced webpage http://lnk.example-short.test/kQ7r, I'd
like a single banner that says "Brisbane's leading Varnel Suite
specialists". In the banner have a computer screen or laptop and a
tablet or smartphone with some 'varnel suite for business' style of
logos coming out of it be creative with some nice design.

Under that, 3 square (or something) icons.
Save Money | Collaborate | Grow
just put some placemarker text in it in a similar fashion to the
reference site.

Just throw some other things in there to fill it up a bit.
Should not have
• http://lnk.example-short.test/kQ7r
I don't want the scrolling banner with the site above, static is fine.

I don't like how when the menu is moused-over, the whole page
moves down.

No stock photos of 'successful business people' or 'very attractive
telephone operator waiting to take your call' :)

```html
<!DOCTYPE html>
<html lang="en">
<head>
<meta charset="utf-8">
<title>CloudLane – Varnel Suite Specialists</title>
<link rel="stylesheet" href="https://fonts.googleapis.com/css2?family=Roboto:ital,wght@0,300;0,400;0,500;0,700;1,400&family=Roboto+Condensed:wght@400;700&display=swap">
<style>
:root{
  --orange:#f6a81c;
  --blue:#2b8fd8;
  --ink:#2e2e2e;
  --text:#8a8a8a;
  --muted:#a5a5a5;
  --line:#e2e2e2;
  --band:#ececec;
  --footer:#555555;
  --footer-text:#d6d6d6;
  --hero-dark:#4a4a4a;
  --hero-light:#8a8a8a;
  --white:#ffffff;
}
*{box-sizing:border-box;margin:0;padding:0}
html,body{width:1200px;height:2343px;overflow:hidden;background:var(--white)}
body{font-family:"Roboto",Arial,sans-serif;color:var(--text);position:relative}

/* header */
.site-header{position:absolute;left:0;top:0;width:1200px;height:92px;background:linear-gradient(#fff,#f1f1f1);border-bottom:1px solid #ddd}
.brand{position:absolute;left:141px;top:24px;display:flex;align-items:center;gap:16px}
.brand-mark{width:44px;height:44px;border-radius:50%;background:var(--blue)}
.brand-name{font-weight:700;font-size:34px;color:#2a2f6e;letter-spacing:-.5px}
.main-nav{position:absolute;left:474px;top:33px;display:flex;gap:8px}
.main-nav a{font-family:"Roboto Condensed",Arial,sans-serif;font-size:15.5px;color:#333;text-decoration:none;padding:5px 9px;border-radius:16px;text-transform:uppercase;white-space:nowrap}
.main-nav a.active{background:var(--blue);color:#fff;box-shadow:inset 0 -2px 0 rgba(0,0,0,.15)}

/* hero */
.hero{position:absolute;left:0;top:92px;width:1200px;height:391px;background:radial-gradient(ellipse at 35% 60%,var(--hero-light),var(--hero-dark) 75%)}
.hero-art{position:absolute;left:196px;top:25px;width:352px;height:343px;border-radius:30px;background:linear-gradient(135deg,#3b3b3b,#7a7a7a 40%,#4fa3d9 70%,#e2733b)}
.hero-title{position:absolute;left:598px;top:112px;padding:14px 22px;background:rgba(0,0,0,.12);font-family:"Roboto Condensed",Arial,sans-serif;font-weight:400;font-size:41px;line-height:46px;color:#fff;text-transform:uppercase;white-space:nowrap}
.hero-title .accent{color:var(--orange)}

/* intro */
.intro{position:absolute;left:0;top:483px;width:1200px;height:182px;text-align:center;background:linear-gradient(#fff 75%,#f3f3f3)}
.intro blockquote{margin-top:28px;font-family:"Roboto Condensed",Arial,sans-serif;font-weight:700;font-size:26px;color:var(--ink)}
.intro p{margin-top:6px;font-size:15px;line-height:21px;color:var(--muted)}
.btn-dark{display:inline-block;margin-top:18px;padding:9px 14px;background:#222;color:#fff;font-family:"Roboto Condensed",Arial,sans-serif;font-weight:700;font-size:16px;border-radius:3px;text-transform:uppercase}

/* features */
.features{position:absolute;left:140px;top:706px;width:920px;display:flex;justify-content:space-between}
.feature{width:300px;text-align:center}
.feature h2{font-family:"Roboto Condensed",Arial,sans-serif;font-weight:700;font-size:28px;color:var(--ink)}
.feature svg{display:block;margin:24px auto 0}
.feature p{margin-top:20px;font-size:13.5px;line-height:21px;color:var(--muted);padding:0 20px}

/* band */
.band{position:absolute;left:0;top:984px;width:1200px;height:282px;background:var(--band);border-top:1px solid #dcdcdc;border-bottom:1px solid #dcdcdc}
.band-inner{position:absolute;left:140px;top:45px;width:920px;display:flex;justify-content:space-between}
.band-col{width:300px;text-align:center}
.band-col h3{font-family:"Roboto Condensed",Arial,sans-serif;font-weight:700;font-size:20px;color:var(--ink);text-transform:uppercase}
.band-col p{margin-top:18px;font-size:13.5px;line-height:21px;color:#777;padding:0 8px}
.btn-light{display:inline-block;margin-top:26px;width:205px;padding:9px 0;background:linear-gradient(#fafafa,#dcdcdc);border:1px solid #ccc;color:#444;font-family:"Roboto Condensed",Arial,sans-serif;font-size:17px;box-shadow:0 12px 10px -10px rgba(0,0,0,.45)}

/* news */
.news-col{position:absolute;top:1298px;width:441px}
.news-col.blog{left:141px}
.news-col.events{left:618px}
.news-head{display:flex;align-items:center;gap:10px;height:28px}
.news-head h3{font-family:"Roboto Condensed",Arial,sans-serif;font-weight:700;font-size:20px;color:#555}
.news-head h3 span{color:var(--orange)}
.news-head small{font-size:11px;font-style:italic;color:var(--muted)}
.news-head .rule{flex:1;height:7px;background:#eee}
.news-item{display:flex;gap:16px;padding:20px 0 14px;border-bottom:1px solid var(--line);height:146px;position:relative}
.thumb{width:70px;height:70px;flex:none;border:2px solid #ccc;background:linear-gradient(135deg,#111,#3a6fb0 50%,#b33a3a)}
.date-box{width:70px;height:80px;flex:none;background:var(--orange);color:#fff;text-align:center;font-family:"Roboto Condensed",Arial,sans-serif;font-weight:700;padding-top:8px}
.date-box b{display:block;font-size:34px;line-height:36px}
.date-box span{font-size:20px}
.news-item h4{font-family:"Roboto Condensed",Arial,sans-serif;font-weight:700;font-size:17px;color:#444;white-space:nowrap}
.news-item p{margin-top:8px;font-size:12.5px;line-height:19px;color:var(--muted)}
.meta{position:absolute;right:0;bottom:14px;display:flex;gap:18px;font-size:11px;font-style:italic;color:var(--muted);align-items:center}
.meta i{display:inline-block;width:12px;height:12px;background:#aaa;border-radius:50%;vertical-align:-2px;margin-right:5px}
.show-all{margin-top:28px;height:28px;line-height:28px;background:#e4e4e4;text-align:center;font-size:12px;font-style:italic;color:#666}

/* customers */
.customers-rule{position:absolute;left:141px;top:1729px;width:918px;height:3px;background:#444}
.customers-tag{position:absolute;left:472px;top:1710px;width:256px;height:40px;line-height:40px;background:#444;color:#fff;text-align:center;font-family:"Roboto Condensed",Arial,sans-serif;font-weight:700;font-size:23px;clip-path:polygon(6% 0,94% 0,100% 50%,94% 100%,6% 100%,0 50%)}
.customers{position:absolute;left:188px;top:1824px;width:824px;display:flex;justify-content:space-between}
.customer{width:180px;text-align:center;font-family:"Roboto Condensed",Arial,sans-serif;font-weight:700;font-size:30px;color:#333;letter-spacing:1px}
.carousel-arrow{position:absolute;top:1822px}

/* footer */
.site-footer{position:absolute;left:0;top:1992px;width:1200px;height:269px;background:var(--footer)}
.foot-col{position:absolute;top:22px;color:var(--footer-text);font-size:12.5px;line-height:22px}
.foot-col h4{font-family:"Roboto Condensed",Arial,sans-serif;font-weight:700;font-size:20px;color:#fff;margin-bottom:14px}
.foot-col ul{list-style:none}
.email-field{margin-top:14px;width:185px;height:28px;border-radius:14px;background:#2f2f2f;color:#bbb;padding-left:14px;line-height:28px}
.btn-orange{display:inline-block;margin-top:12px;padding:0 10px;height:26px;line-height:26px;border-radius:13px;background:var(--orange);color:#fff;font-weight:700;font-size:12px;text-transform:uppercase}
.contact-list{margin-top:16px}
.contact-line{display:flex;align-items:center;gap:10px;height:28px;white-space:nowrap}
.contact-line i{width:12px;height:12px;background:#ddd;border-radius:2px;flex:none}
.contact-line em{font-style:normal;color:var(--orange)}
.footer-bar{position:absolute;left:0;top:2261px;width:1200px;height:82px;background:#fff}
.footer-brand{position:absolute;left:141px;top:16px;display:flex;align-items:center;gap:16px}
.footer-brand .brand-mark{background:#222}
.footer-brand .brand-name{color:#222}
.copyright{position:absolute;left:476px;top:52px;font-size:11px;color:#777}
.social{position:absolute;left:806px;top:0;width:394px;height:82px;background:var(--footer);border-top-left-radius:60px 24px}
.social p{position:absolute;left:55px;top:6px;color:#fff;font-size:12px}
.social ul{position:absolute;left:55px;top:40px;display:flex;gap:10px;list-style:none}
.social li{width:31px;height:31px;border-radius:4px;background:#8fa7b8}
.to-top{position:absolute;left:578px;top:2232px;width:40px;height:40px}
</style>
</head>
<body>

<header class="site-header">
  <div class="brand"><span class="brand-mark"></span><span class="brand-name">CloudLane</span></div>
  <nav class="main-nav">
    <a class="active" href="#">About</a><a href="#">Support</a><a href="#">Deployment</a><a href="#">Training</a><a href="#">Development</a><a href="#">Contact Us</a>
  </nav>
</header>

<section class="hero">
  <div class="hero-art" role="img" aria-label="Smartphone with colourful app icons flying out of its screen"></div>
  <h1 class="hero-title">Brisbane's leading<br><span class="accent">Varnel Suite</span> specialists</h1>
</section>

<section class="intro">
  <blockquote>“Lorem Ipsum is simply dummy text of the printing and typesetting industry.”</blockquote>
  <p>Lorem Ipsum has been the industry's standard dummy text ever since the 1500s,<br>when an unknown printer took a galley of type and scrambled it to make a type specimen book.</p>
  <span class="btn-dark">Ask your question ?</span>
</section>

<section class="features">
  <div class="feature">
    <h2>Save Money</h2>
    <svg width="70" height="70" viewBox="0 0 70 70"><circle cx="35" cy="35" r="32" fill="none" stroke="#999" stroke-width="3"/><circle cx="35" cy="35" r="22" fill="#999"/><text x="35" y="45" text-anchor="middle" font-family="Roboto,sans-serif" font-weight="700" font-size="28" fill="#fff">$</text></svg>
    <p>Lorem ipsum dolor sit amet, Lorem Ipsum, dizgi ve baskı endüstrisinde kullanılan consec-tetur adipiscing elit ...</p>
  </div>
  <div class="feature">
    <h2>Collaborate</h2>
    <svg width="70" height="70" viewBox="0 0 70 70" fill="none" stroke="#999" stroke-width="2.5"><circle cx="35" cy="35" r="32"/><circle cx="35" cy="35" r="5" fill="#999"/><circle cx="35" cy="15" r="4"/><circle cx="53" cy="28" r="4"/><circle cx="47" cy="51" r="4"/><circle cx="23" cy="51" r="4"/><circle cx="17" cy="28" r="4"/><path d="M35 30V19M40 33l9-4M38 39l7 9M32 39l-7 9M30 33l-9-4"/></svg>
    <p>Lorem ipsum dolor sit amet, Lorem Ipsum, dizgi ve baskı endüstrisinde kullanılan consec-tetur adipiscing elit ...</p>
  </div>
  <div class="feature">
    <h2>Grow</h2>
    <svg width="70" height="70" viewBox="0 0 70 70" fill="#999"><rect x="6" y="52" width="5" height="10"/><rect x="14" y="48" width="5" height="14"/><rect x="22" y="50" width="5" height="12"/><rect x="30" y="42" width="5" height="20"/><rect x="38" y="34" width="5" height="28"/><rect x="46" y="26" width="5" height="36"/><rect x="54" y="16" width="5" height="46"/><path d="M6 44l14-8 10 4 24-28" fill="none" stroke="#999" stroke-width="2"/></svg>
    <p>Lorem ipsum dolor sit amet, Lorem Ipsum, dizgi ve baskı endüstrisinde kullanılan consec-tetur adipiscing elit ...</p>
  </div>
</section>

<section class="band">
  <div class="band-inner">
    <div class="band-col"><h3>Run your business in the cloud</h3><p>Lorem Ipsum is simply dummy text of the printing and typesetting industry. Lorem Ipsum has been the industry's standard dummy text ever since the 1500s,</p><span class="btn-light">Explore Our Apps Solutions</span></div>
    <div class="band-col"><h3>How can we help you?</h3><p>Lorem Ipsum is simply dummy text of the printing and typesetting industry. Lorem Ipsum has been the industry's standard dummy text ever since the 1500s,</p><span class="btn-light">Explore Our Apps Solutions</span></div>
    <div class="band-col"><h3>Learn from Cloud Guides</h3><p>Lorem Ipsum is simply dummy text of the printing and typesetting industry. Lorem Ipsum has been the industry's standard dummy text ever since the 1500s,</p><span class="btn-light">Explore Our Apps Solutions</span></div>
  </div>
</section>

<section class="news-col blog">
  <div class="news-head"><h3>Recent <span>Blog</span></h3><small>get latest updates</small><div class="rule"></div></div>
  <article class="news-item">
    <div class="thumb" role="img" aria-label="Blog post thumbnail"></div>
    <div><h4>The standard Lorem Ipsum used since the 1500s !!!</h4><p>Contrary to popular belief, Lorem Ipsum is not simply random It has roots in a piece of classical Latin literature from 45 BC...</p></div>
    <div class="meta"><span><i></i>15 Nov, 2012</span><span><i></i>12 Comments</span></div>
  </article>
  <article class="news-item">
    <div class="thumb" role="img" aria-label="Blog post thumbnail"></div>
    <div><h4>The standard Lorem Ipsum used since the 1500s !!!</h4><p>Contrary to popular belief, Lorem Ipsum is not simply random It has roots in a piece of classical Latin literature from 45 BC...</p></div>
    <div class="meta"><span><i></i>15 Nov, 2012</span><span><i></i>12 Comments</span></div>
  </article>
  <div class="show-all">Show All Blog</div>
</section>

<section class="news-col events">
  <div class="news-head"><h3>Upcoming <span>Events</span></h3><small>get latest updates</small><div class="rule"></div></div>
  <article class="news-item">
    <div class="date-box"><b>20</b><span>DEC</span></div>
    <div><h4>The standard Lorem Ipsum used since the 1500s !!!</h4><p>Contrary to popular belief, Lorem Ipsum is not simply random It has roots in a piece of classical Latin literature from 45 BC...</p></div>
    <div class="meta"><span><i></i>Live Event</span><span><i></i>Cloud Hall</span><span><i></i>Continue Reading...</span></div>
  </article>
  <article class="news-item">
    <div class="date-box"><b>20</b><span>DEC</span></div>
    <div><h4>The standard Lorem Ipsum used since the 1500s !!!</h4><p>Contrary to popular belief, Lorem Ipsum is not simply random It has roots in a piece of classical Latin literature from 45 BC...</p></div>
    <div class="meta"><span><i></i>Live Event</span><span><i></i>Cloud Hall</span><span><i></i>Continue Reading...</span></div>
  </article>
  <div class="show-all">Show All Events</div>
</section>

<div class="customers-rule"></div>
<div class="customers-tag">OUR CUSTOMERS</div>
<svg class="carousel-arrow" style="left:139px" width="34" height="60" viewBox="0 0 34 60"><path d="M32 2L3 30l29 28" fill="none" stroke="#bbb" stroke-width="2"/></svg>
<svg class="carousel-arrow" style="left:1027px" width="34" height="60" viewBox="0 0 34 60"><path d="M2 2l29 28L2 58" fill="none" stroke="#bbb" stroke-width="2"/></svg>
<section class="customers">
  <div class="customer">RIDGELINE</div><div class="customer">RIDGELINE</div><div class="customer">RIDGELINE</div><div class="customer">RIDGELINE</div>
</section>

<footer class="site-footer">
  <div class="foot-col" style="left:160px;width:190px">
    <h4>Newsletter !</h4>
    <p>Enter your email to receive news &amp; updates.</p>
    <div class="email-field">Enter email</div>
    <span class="btn-orange">Subscribe</span>
  </div>
  <div class="foot-col" style="left:436px">
    <h4>Quick Links</h4>
    <ul><li>About</li><li>Support</li><li>Deployment</li><li>Training</li><li>Development</li><li>Contact Us</li></ul>
  </div>
  <div class="foot-col" style="left:681px">
    <h4>Services</h4>
    <ul><li>Save Money</li><li>Collaborate</li><li>Grow</li></ul>
  </div>
  <div class="foot-col" style="left:859px;width:270px">
    <h4>Contact us</h4>
    <p>Lorem ipsum dolor sit amet, odio<br>consectetur adipiscing elit.</p>
    <div class="contact-list">
      <div class="contact-line"><i></i>Lorem ipsum, State, Country</div>
      <div class="contact-line"><i></i>Tel.: <em>+48 500 000 123</em></div>
      <div class="contact-line"><i></i>E-mail: <em>office@example-mail.test</em></div>
      <div class="contact-line"><i></i>Your-Skype-Name</div>
    </div>
  </div>
</footer>

<div class="footer-bar">
  <div class="footer-brand"><span class="brand-mark"></span><span class="brand-name">CloudLane</span></div>
  <p class="copyright">Copyright © 2012 CloudLane. All Rights Reserved.</p>
  <div class="social">
    <p>Visit also our social profiles:</p>
    <ul><li></li><li></li><li></li><li></li><li></li></ul>
  </div>
</div>
<svg class="to-top" viewBox="0 0 40 40"><circle cx="20" cy="20" r="19" fill="#fff" stroke="#ccc"/><path d="M20 28V13M14 19l6-6 6 6" fill="none" stroke="#555" stroke-width="2.5"/></svg>

</body>
</html>
```